RM Trovenix businesscard project

RM Cargoline Ltd is a freshly founded small (3 employees), young (average age is 30 years) company, living from the road transportation market without own tools.
We would like to have an impressive, new-line, cool busines card for a freshly founded forwarding company on an overcrowded market which raises attention and makes the potential partners eager to work with us.

Target Market(s)

The main profile of the company is logistic/forwarding on road.

Industry/Entity Type

Freight Forwarding

Contact Information for Business Card

Name: Berki Zsófia
Title: general manager
mobile nr: +36-00/555-0142
fax nr: +36-0/555-0198
e-mail: zsofia.berki@rmtrovenix.example
info@rmtrovenix.example
website address: http://www.rmtrovenix.example
and if possible maybe some funny or helpful info on the back

Requirements
Must have
• contact details above
Nice to have
• some really nice and catching back-side (info, graphics, useful tool info... anything)
Should not have
• trucks, road, ship, airplane on it...

```html
<!DOCTYPE html>
<html lang="hu">
<head>
<meta charset="utf-8">
<title>RM Trovenix – Business Card</title>
<link rel="stylesheet" href="https://fonts.googleapis.com/css2?family=Open+Sans:wght@400;600&display=swap">
<style>
  :root {
    --side-top: #e4e4e4;
    --side-bottom: #ffffff;
    --blue-top: #05689f;
    --blue-bottom: #4497c6;
    --badge-bg: #ebebeb;
    --badge-ink: #3b3431;
    --accent: #5a86bd;
    --text-light: #ffffff;
  }
  html, body {
    margin: 0;
    padding: 0;
    width: 1200px;
    height: 600px;
    overflow: hidden;
    background: #ffffff;
  }
  .card {
    position: relative;
    width: 1200px;
    height: 600px;
    overflow: hidden;
    font-family: "Open Sans", "Segoe UI", sans-serif;
    background: linear-gradient(to bottom, var(--blue-top), var(--blue-bottom));
  }
  .side-band {
    position: absolute;
    left: 0;
    top: 0;
    width: 273px;
    height: 600px;
    background: linear-gradient(to bottom, var(--side-top), var(--side-bottom));
  }
  .brand-badge {
    position: absolute;
    left: 140px;
    top: 130px;
    width: 250px;
    height: 282px;
    background: var(--badge-bg);
    box-shadow: 2px 3px 6px rgba(0, 0, 0, 0.35);
    display: flex;
    flex-direction: column;
    align-items: center;
    justify-content: flex-end;
    padding-bottom: 22px;
    box-sizing: border-box;
  }
  .brand-square {
    width: 96px;
    height: 96px;
    background: var(--accent);
    margin-bottom: 54px;
  }
  .brand-name {
    font-size: 36px;
    font-weight: 400;
    line-height: 48px;
    color: var(--badge-ink);
    white-space: nowrap;
  }
  .details {
    position: absolute;
    left: 469px;
    top: 108px;
    width: 600px;
    text-align: center;
    color: var(--text-light);
  }
  .person-name {
    margin: 0;
    font-size: 45px;
    font-weight: 400;
    line-height: 62px;
  }
  .person-title {
    margin: 0;
    font-size: 28px;
    font-weight: 400;
    line-height: 34px;
  }
  .contact-list {
    list-style: none;
    margin: 68px 0 0;
    padding: 0;
    font-size: 31px;
    line-height: 41px;
    white-space: nowrap;
  }
</style>
</head>
<body>
  <div class="card">
    <div class="side-band"></div>
    <div class="brand-badge">
      <div class="brand-square"></div>
      <div class="brand-name">RM Trovenix</div>
    </div>
    <div class="details">
      <h1 class="person-name">Berki Zsófia</h1>
      <p class="person-title">General Manager</p>
      <ul class="contact-list">
        <li>Mobile No : +36-00/555-0142</li>
        <li>Fax No : +36-0/555-0198</li>
        <li>e-mail : zsofia.berki@rmtrovenix.example</li>
        <li>info@rmtrovenix.example</li>
        <li>Website : http://www.rmtrovenix.example</li>
      </ul>
    </div>
  </div>
</body>
</html>
```